Chicago Property Management Flyer

We need a brochure/flyer to market our property management services to Chicago property owners. I believe that my preference is single page, double sided, but a bi-fold or tri-fold format may also work. I have provided our logo, and some example images in case that is helpful. Refer to our website at http://www.lumevarpm.net/ for more info.

Industry/Entity Type

Property Management

Font styles to use
Sans Serif

```html
<!DOCTYPE html>
<html lang="en">
<head>
<meta charset="utf-8">
<title>Lumevar Property Management Flyer</title>
<link href="https://fonts.googleapis.com/css2?family=Roboto:wght@300;400;500;700&display=swap" rel="stylesheet">
<style>
  :root {
    --brand-blue: #1c5486;
    --heading-blue: #1f4f7e;
    --body-gray: #6b6b6b;
    --band-gray: #e2e2e2;
    --page-white: #ffffff;
    --backdrop: #ecebe8;
  }
  * { margin: 0; padding: 0; box-sizing: border-box; }
  html, body { width: 1040px; height: 1200px; overflow: hidden; }
  body {
    background: var(--backdrop);
    font-family: "Roboto", Arial, sans-serif;
    position: relative;
  }
  .page {
    position: absolute;
    top: 233px;
    width: 438px;
    height: 679px;
    background: var(--page-white);
    overflow: hidden;
  }
  .page--front { left: 66px; }
  .page--back { left: 531px; }
  .top-band {
    position: absolute; left: 0; top: 0; width: 100%; height: 11px;
    background: var(--band-gray);
  }
  .front-triangle { position: absolute; left: 176px; top: 0; }
  .brand-name {
    position: absolute; left: 0; top: 158px; width: 100%;
    display: flex; justify-content: center; align-items: center; gap: 8px;
    color: var(--brand-blue); font-weight: 700; font-size: 14px; letter-spacing: 0.3px;
  }
  .brand-mark { width: 10px; height: 10px; background: var(--brand-blue); }
  .front-tagline {
    position: absolute; left: 0; top: 223px; width: 100%;
    text-align: center; color: var(--brand-blue);
    font-weight: 300; font-size: 18px; line-height: 22px;
  }
  .skyline-photo {
    position: absolute; left: 0; top: 315px; width: 100%; height: 323px;
    background: linear-gradient(180deg, #f5f7f8 0%, #e4e9ec 35%, #a9b3ba 62%, #6f757a 100%);
  }
  .front-contacts {
    position: absolute; left: 0; top: 638px; width: 100%; height: 41px;
    display: flex; justify-content: space-around; align-items: center;
    color: var(--heading-blue); font-size: 12px; padding: 0 12px;
  }
  .intro-list { position: absolute; left: 43px; top: 55px; width: 380px; list-style: none; }
  .intro-list li {
    position: relative; padding-left: 22px; margin-bottom: 19px;
    color: var(--brand-blue); font-size: 15.5px; line-height: 19px; font-weight: 400;
  }
  .intro-list li::before {
    content: ""; position: absolute; left: 0; top: 9px; width: 5px; height: 5px;
    background: var(--brand-blue); transform: rotate(20deg);
  }
  .building-photo {
    position: absolute; left: 26px; top: 180px; width: 401px; height: 222px;
    background: linear-gradient(180deg, #9c5a48 0%, #8a4e3f 55%, #4f6a35 80%, #7a9a4a 100%);
  }
  .service {
    position: absolute; width: 198px;
  }
  .service h3 {
    color: var(--heading-blue); font-weight: 400; font-size: 11.6px; line-height: 13px;
  }
  .service p {
    color: var(--body-gray); font-size: 8.4px; line-height: 11.6px;
  }
  .col-left { left: 26px; }
  .col-right { left: 233px; }
  .back-footer {
    position: absolute; left: 0; top: 640px; width: 100%; height: 39px;
    background: var(--band-gray);
    display: flex; align-items: center; padding-left: 26px;
    color: var(--heading-blue); font-size: 10px;
  }
</style>
</head>
<body>

<section class="page page--front">
  <div class="top-band"></div>
  <svg class="front-triangle" width="86" height="74" viewBox="0 0 86 74">
    <polygon points="0,0 86,0 43,74" fill="#1c5486"/>
  </svg>
  <div class="brand-name"><span class="brand-mark"></span>LUMEVAR PROPERTY MANAGEMENT</div>
  <p class="front-tagline">Managing Properties Over Chicago<br>for over a decade</p>
  <div class="skyline-photo" role="img" aria-label="Aerial photo of the Chicago downtown skyline beside the lake"></div>
  <div class="front-contacts">
    <span>312-555-0148</span>
    <span>www.lumevarpm.net</span>
    <span>dana@lumevarpm.net</span>
  </div>
</section>

<section class="page page--back">
  <div class="top-band"></div>
  <ul class="intro-list">
    <li>Managing HCV / Section 8 rentals across Chicago for over a decade.</li>
    <li>Leverage our experience and expertise to succeed with your properties.</li>
  </ul>
  <div class="building-photo" role="img" aria-label="Photo of a red brick Chicago apartment building with iron fence and lawn"></div>

  <div class="service col-left" style="top:420px">
    <h3>Save Time and Headaches</h3>
    <p>We have a team in place to tackle all aspects of property management for you. Never worry about leasing, tenants, maintenance, regulations, etc.</p>
  </div>
  <div class="service col-left" style="top:492px">
    <h3>Maximize Your Investment Assets</h3>
    <p>Your properties are expensive assets with lots of potential. Put the right professionals in place to protect, maintain, and maximize their value.</p>
  </div>
  <div class="service col-left" style="top:564px">
    <h3>Increase Income</h3>
    <p>With our experience and market knowledge we can establish optimal rent prices, lease apartments quickly, reduce turnover, and navigate complex housing agency processes to ensure maximum income to you.</p>
  </div>

  <div class="service col-right" style="top:417px">
    <h3>Reduce Expenses, Maximize Profits</h3>
    <p>Maximize your profits by benefitting from our economies of scale, systems and processes, specialized knowledge, industry network, and buying power</p>
  </div>
  <div class="service col-right" style="top:491px">
    <h3>Stay Informed</h3>
    <p>With access to all of your property information, documentation, and financials through your online portal of our property management system you and your accountant can stay informed as needed</p>
  </div>
  <div class="service col-right" style="top:577px">
    <h3>Grow Your Investment Portfolio</h3>
    <p>With our management team focused on profitably managing your existing properties, we can then help you expand to future investments</p>
  </div>

  <div class="back-footer">Lumevar Property Management: 1180 W. Hollis Ave Chicago IL 60607 312-555-0148</div>
</section>

</body>
</html>
```